A Hair, Beauty and Nails Wholesalers Needs a Business Card Design

We need a business card design for our company which is being passed from parents to daughter, so we wont to re-launch the company with an updated, modern, sophisticated, elegant, chic and fresh look which still incorporates the original colour scheme of Hot Pink, Dark Grey and White. The original logo which is attached can be used on the card but we would like to see some designs with the logo and some without, as we have not yet decided if we want the logo on the card. The name of our company is 'Velmora Supplies' and the name of our website is VelmoraGlowandPolish.example.au. We specialise in supplying a massive range of Hair, Beauty and Nail products to the industry. We are based in QLD, Australia but ship many orders via our website all across Australia.

```html
<!DOCTYPE html>
<html lang="en">
<head>
<meta charset="utf-8">
<title>Velmora Supplies – Business Card</title>
<link href="https://fonts.googleapis.com/css2?family=Arimo:wght@400&family=Tinos:wght@700&display=swap" rel="stylesheet">
<style>
  :root {
    --hot-pink: #e0107a;
    --soft-pink: #f0b6d4;
    --blush: #f3d3e4;
    --card-white: #fbf8fa;
    --dark-grey: #2b2b2f;
    --mid-grey: #6f6f75;
    --backdrop: #e7e5e8;
  }
  * { box-sizing: border-box; margin: 0; padding: 0; }
  html, body { width: 1200px; height: 960px; overflow: hidden; }
  body {
    background: var(--backdrop);
    display: flex;
    align-items: center;
    justify-content: center;
    gap: 100px;
    font-family: "Arimo", Arial, sans-serif;
  }
  .card {
    width: 360px;
    height: 620px;
    background: linear-gradient(180deg, var(--card-white) 0%, var(--card-white) 45%, var(--blush) 100%);
    box-shadow: 0 10px 30px rgba(0,0,0,0.18);
    position: relative;
    display: flex;
    flex-direction: column;
    align-items: center;
  }
  .brand-mark {
    width: 230px;
    height: 150px;
    border-radius: 48% 52% 40% 45% / 55% 55% 40% 40%;
    background: radial-gradient(ellipse at 45% 40%, var(--hot-pink) 0%, #e84d9b 60%, var(--soft-pink) 100%);
  }
  .brand-name {
    margin-top: 14px;
    font-size: 17px;
    color: var(--mid-grey);
    letter-spacing: 0.5px;
  }
  .card--front .brand-mark { margin-top: 110px; }
  .company-name {
    margin-top: 60px;
    font-family: "Tinos", "Times New Roman", serif;
    font-weight: 700;
    font-size: 40px;
    color: var(--hot-pink);
    text-align: center;
    white-space: nowrap;
    line-height: 1.1;
  }
  .card--back .brand-mark { margin-top: 60px; }
  .contact-block {
    margin-top: 48px;
    width: 100%;
    padding: 0 30px;
  }
  .person-name {
    font-family: "Tinos", "Times New Roman", serif;
    font-weight: 700;
    font-size: 31px;
    color: var(--hot-pink);
    white-space: nowrap;
  }
  .person-role {
    font-size: 17px;
    color: var(--dark-grey);
    margin-bottom: 22px;
  }
  .contact-line {
    font-size: 15px;
    color: var(--dark-grey);
    line-height: 1.6;
    white-space: nowrap;
  }
</style>
</head>
<body>
  <section class="card card--front">
    <div class="brand-mark" role="img" aria-label="Illustrated hair made of pink beauty tool icons"></div>
    <p class="brand-name">Velmora Glow and Polish</p>
    <h1 class="company-name">Velmora Supplies</h1>
  </section>

  <section class="card card--back">
    <div class="brand-mark" role="img" aria-label="Illustrated hair made of pink beauty tool icons"></div>
    <p class="brand-name">Velmora Glow and Polish</p>
    <div class="contact-block">
      <h2 class="person-name">Danielle Harwood</h2>
      <p class="person-role">Manager</p>
      <p class="contact-line">58 Marlow Street</p>
      <p class="contact-line">BRENTHAVEN, QLD, 4871</p>
      <p class="contact-line">(07) 5550 0142</p>
      <p class="contact-line">admin@velmoraglowandpolish.example.au</p>
      <p class="contact-line">www.velmoraglowandpolish.example.au</p>
    </div>
  </section>
</body>
</html>
```